Tandrel needs stationery design

We need desings for presentation cards and letter head for our company. It would be better that the letterhead uses our logo with white background and the presentation card the logo with the black background for the back of the card and the text (name, phone

Colors
0455a3
ec1f27
000000

Requirements
Must have
• Use company logo and colors

```html
<!DOCTYPE html>
<html lang="en">
<head>
<meta charset="utf-8">
<title>Tandrel Stationery</title>
<link href="https://fonts.googleapis.com/css2?family=Lato:wght@400;700;900&display=swap" rel="stylesheet">
<style>
:root{
  --blue:#0455a3;
  --red:#ec1f27;
  --black:#000000;
  --ink:#333333;
  --muted:#666666;
  --rule:#bdbdbd;
  --paper:#ffffff;
  --stage:#e9e9e9;
}
*{margin:0;padding:0;box-sizing:border-box}
html,body{width:1200px;height:971px;overflow:hidden}
body{background:var(--stage);font-family:'Lato',sans-serif;color:var(--ink);position:relative}

.brand{display:flex;align-items:center;gap:6px;font-weight:900;letter-spacing:.12em;color:var(--black);white-space:nowrap}
.brand-dot{width:8px;height:8px;background:var(--red);border-radius:50%;flex:none}

/* Letterhead */
.letterhead{position:absolute;left:540px;top:40px;width:622px;height:880px;background:var(--paper);
  box-shadow:0 6px 24px rgba(0,0,0,.12);padding:56px 58px 50px}
.letterhead .brand{font-size:22px}
.lh-top{display:flex;justify-content:space-between;align-items:flex-start}
.date{font-size:11px;color:var(--ink);margin-top:10px}
.date span{display:inline-block;width:70px;border-bottom:1px solid var(--rule);margin-left:4px}
.contact-block{margin-top:30px;font-size:8px;line-height:1.55;color:var(--muted)}
.contact-block b{font-weight:700;color:var(--ink)}
.salutation{margin-top:44px;font-size:11px}
.salutation span{display:inline-block;width:60px;border-bottom:1px solid var(--rule)}
.body-text{margin-top:26px;font-size:11px;line-height:1.6;color:var(--muted)}
.body-text p{margin-bottom:18px}
.body-text p.strong{font-weight:700;color:var(--ink)}
.sign{margin-top:60px}
.signature-area{width:140px;height:46px;background:linear-gradient(90deg,#eef2fa,#dfe6f4);border-bottom:1px solid var(--ink)}
.sign-name{margin-top:8px;font-size:12px;font-weight:700;color:var(--ink)}
.sign-role{font-size:9px;color:var(--muted)}

/* Cards */
.card{position:absolute;left:40px;width:420px;height:240px;box-shadow:0 6px 18px rgba(0,0,0,.18)}
.card-back{top:300px}
.card-back .pattern{position:absolute;inset:0;background:linear-gradient(135deg,#1a1a1a,#0a0a0a)}
.card-back .brand{position:absolute;left:50%;top:50%;transform:translate(-50%,-50%);color:var(--paper);font-size:28px}
.card-front{top:590px;background:var(--paper);padding:24px 34px;display:flex;flex-direction:column;align-items:center;justify-content:center}
.card-front .brand{font-size:26px}
.rule{width:100%;height:1px;background:var(--rule)}
.card-front .rule.top{margin-top:12px}
.person{text-align:center;margin:10px 0 12px}
.person-name{font-size:13px;font-weight:900;color:var(--black);letter-spacing:.04em}
.person-role{font-size:8px;font-weight:700;color:var(--blue);letter-spacing:.1em}
.card-details{display:flex;width:100%;margin-top:14px;font-size:9px;color:var(--black);font-weight:700}
.card-details .col{flex:1;display:flex;flex-direction:column;gap:6px}
.card-details .col.left{align-items:flex-end;padding-right:14px;border-right:1px solid var(--rule)}
.card-details .col.right{padding-left:14px}
.item{display:flex;align-items:center;gap:6px;white-space:nowrap}
.item svg{width:9px;height:9px;fill:var(--red);flex:none}
</style>
</head>
<body>

<section class="letterhead">
  <header class="lh-top">
    <div class="brand"><span class="brand-dot"></span>TANDREL</div>
    <div class="date">Date :<span></span></div>
  </header>
  <div class="contact-block">
    <div><b>Phone :</b> (+010) 555 014 2</div>
    <div><b>Email :</b> hello@tandrel-co.com</div>
    <div><b>Web address :</b> www.tandrel-co.com</div>
    <div><b>Address :</b> 214 Harbor Ln. Westfield,<br>ST 00000</div>
  </div>
  <p class="salutation">Dear, Mr <span></span></p>
  <div class="body-text">
    <p>Lorem Ipsum is simply dummy text of the printing and typesetting industry. Lorem Ipsum has been the industry's standard dummy text ever since the 1500s, when an unknown printer took a galley of type and scrambled it to make a type specimen book. It has survived not only five centuries, but also the leap into electronic typesetting, remaining essentially unchanged. It was popularised in the 1960s with the release of Lettrafix sheets containing Lorem Ipsum passages, and more recently with desktop publishing software like Pagewright Studio including versions of Lorem Ipsum.</p>
    <p class="strong">Lorem Ipsum is simply dummy text of the printing and typesetting industry. Lorem Ipsum has been the industry's standard dummy text ever since the 1500s, when an unknown printer took a galley of type and scrambled it to make a type specimen book.</p>
    <p>Lorem Ipsum is simply dummy text of the printing and typesetting industry. Lorem Ipsum has been the industry's standard dummy text ever since the 1500s, when an unknown printer took a galley of type and scrambled it to make a type specimen book. It has survived not only five centuries, but also the leap into electronic typesetting, remaining essentially unchanged.</p>
    <p>Lorem Ipsum is simply dummy text of the printing and typesetting industry.</p>
  </div>
  <div class="sign">
    <div class="signature-area" role="img" aria-label="Handwritten signature"></div>
    <div class="sign-name">Your Name</div>
    <div class="sign-role">Designation</div>
  </div>
</section>

<section class="card card-back">
  <div class="pattern" role="img" aria-label="Black geometric triangle pattern"></div>
  <div class="brand"><span class="brand-dot"></span>TANDREL</div>
</section>

<section class="card card-front">
  <div class="brand"><span class="brand-dot"></span>TANDREL</div>
  <div class="rule top"></div>
  <div class="person">
    <div class="person-name">YOUR NAME</div>
    <div class="person-role">DESIGNATION</div>
  </div>
  <div class="rule"></div>
  <div class="card-details">
    <div class="col left">
      <div class="item">(+010) 555 014 2
        <svg viewBox="0 0 24 24"><path d="M6.6 10.8a15.1 15.1 0 0 0 6.6 6.6l2.2-2.2a1 1 0 0 1 1-.25 11.4 11.4 0 0 0 3.6.57 1 1 0 0 1 1 1V20a1 1 0 0 1-1 1A17 17 0 0 1 3 4a1 1 0 0 1 1-1h3.5a1 1 0 0 1 1 1c0 1.25.2 2.45.57 3.57a1 1 0 0 1-.25 1z"/></svg>
      </div>
      <div class="item">hello@tandrel-co.com
        <svg viewBox="0 0 24 24"><path d="M2 5h20v14H2z M4 7v.5l8 5 8-5V7l-8 5z"/></svg>
      </div>
    </div>
    <div class="col right">
      <div class="item">
        <svg viewBox="0 0 24 24"><circle cx="12" cy="12" r="10"/></svg>www.tandrel-co.com
      </div>
      <div class="item">
        <svg viewBox="0 0 24 24"><path d="M12 2a7 7 0 0 0-7 7c0 5 7 13 7 13s7-8 7-13a7 7 0 0 0-7-7zm0 9.5A2.5 2.5 0 1 1 12 6.5a2.5 2.5 0 0 1 0 5z"/></svg>214 Harbor Ln. Westfield, ST 00000
      </div>
    </div>
  </div>
</section>

</body>
</html>
```